Professional & Modern Technology Business Card

We need a business card for our software/technology firm. Our services include Program/Project Management, Project Controls and Enterprise Analytics. Our clients are usually in the Aviation, Public Works, Transportation and Electric & Water Utility industries. We serve both public and private clients. Would like a very professional, conservative but somewhat modern design. Design, Develop, Deploy is the corporate tagline. We have two offices. The headquarters is in Atlanta, GA and a satellite office In Savannah, GA. Corporate Logo Attached.
Looking to do website and corporate brochure after the successful completion of this project. Would like to begin a working relationship with best designers.
Tagline: Design, Develop, Deploy
Website: www.quelvanesystems.example
My Name: Marla Dunstead
My Title: CEO
Email: mdunstead@quelvanesystems.example
Atlanta Address:
87 Corliss Avenue, #2291
Atlanta, GA 30301
Office: 404.555.0182
Fax: 404.555.0147
Mobile: 404.555.0163
Savannah Address:
350 West Harrow Bend Road
Suite 720
Savannah, GA 31401
Office: 912.555.0139
Fax: 404.555.0147
Mobile: 404.555.0163
Updates
Please include the email address in your designs: mdunstead@quelvanesystems.example.
I appreciate everyone's design efforts. Just a few notes:
1. Please remove the mobile number from the cards
2. The backs of the cards can be utilized for writing notes. Make sure your design on the back of the card is conducive to clearly adding writing if needed.
3. No black backgrounds please
4. Only use the corporate logo on the front of the card. You can use portions of the logo design, but not the logo in totality.
Thank You
Industry/Entity Type
Conservative
Look and feel
Each slider illustrates characteristics of the customer's brand and the style your logo design should communicate.

```html
<!DOCTYPE html>
<html lang="en">
<head>
<meta charset="utf-8">
<title>Quelvane Systems, Inc. — Business Card Concepts</title>
<link rel="stylesheet" href="https://fonts.googleapis.com/css2?family=Open+Sans:ital,wght@0,300;0,400;0,600;0,700;1,700&display=swap">
<style>
  :root {
    --ink: #222222;
    --name-grey: #333333;
    --frame: #2b2b2b;
    --band-blue: #0a93d5;
    --office-green: #17a05d;
    --office-orange: #ef8a2d;
    --mark-yellow: #e8c21a;
    --paper: #ffffff;
  }
  * { box-sizing: border-box; margin: 0; padding: 0; }
  html, body {
    width: 1200px; height: 773px; overflow: hidden;
    background: var(--paper);
    font-family: "Open Sans", Arial, sans-serif;
    color: var(--ink);
  }
  .sheet { position: relative; width: 1200px; height: 773px; }

  .card {
    position: absolute; width: 579px; height: 350px;
    background: var(--paper);
    border: 1px solid var(--frame);
    overflow: hidden;
  }
  .card--front-a { left: 18px;  top: 20px; }
  .card--back-a  { left: 609px; top: 20px; }
  .card--front-b { left: 18px;  top: 411px; }
  .card--back-b  { left: 609px; top: 411px; }

  .web-band {
    position: absolute; left: 0; right: 0; bottom: 0; height: 32px;
    background: var(--band-blue);
    color: #fff; font-size: 14px; line-height: 32px;
    display: flex; justify-content: center;
  }
  .web-band--split { justify-content: space-between; padding: 0 18px 0 19px; }

  /* Company name lockup */
  .brand { position: absolute; display: flex; align-items: center; gap: 10px; }
  .brand__dot {
    width: 30px; height: 30px; border-radius: 50%;
    background: var(--mark-yellow); flex: none;
  }
  .brand__name {
    font-weight: 600; color: var(--name-grey);
    font-size: 22px; line-height: 1.05; letter-spacing: -0.3px;
  }
  .brand--large .brand__dot { width: 44px; height: 44px; }
  .brand--large .brand__name { font-size: 33px; }
  .card--back-a .brand, .card--back-b .brand {
    left: 50%; top: 147px; transform: translate(-50%, -50%);
  }

  .person__name { font-weight: 300; font-size: 21px; line-height: 24px; color: var(--name-grey); white-space: nowrap; }
  .person__title { font-size: 16px; line-height: 20px; color: var(--name-grey); }

  .tagline { position: absolute; font-weight: 700; font-style: italic; white-space: nowrap; }

  .office { position: absolute; font-size: 14px; line-height: 20px; white-space: nowrap; font-style: normal; }
  .office--atlanta { color: var(--office-green); }
  .office--savannah { color: var(--office-orange); }
  .office--right { text-align: right; }

  /* Front A */
  .card--front-a .brand { left: 30px; top: 112px; }
  .card--front-a .person { position: absolute; right: 344px; top: 202px; text-align: right; }
  .card--front-a .tagline { right: 344px; top: 284px; font-size: 14px; line-height: 20px; }
  .card--front-a .divider {
    position: absolute; left: 262px; top: 58px; width: 2px; height: 234px;
    background: var(--ink);
  }
  .card--front-a .office--atlanta { left: 300px; top: 60px; }
  .card--front-a .office--savannah { left: 300px; top: 174px; }
  .card--front-a .email {
    position: absolute; left: 300px; top: 284px;
    font-size: 14px; line-height: 20px; white-space: nowrap;
  }

  /* Front B */
  .card--front-b .person { position: absolute; left: 20px; top: 28px; }
  .card--front-b .person__title { text-align: right; width: 135px; }
  .card--front-b .brand { right: 16px; top: 30px; }
  .card--front-b .tagline { left: 0; right: 0; text-align: center; top: 132px; font-size: 17px; line-height: 24px; }
  .card--front-b .office--atlanta { left: 19px; top: 208px; }
  .card--front-b .office--savannah { right: 18px; top: 208px; }
</style>
</head>
<body>
<main class="sheet">

  <section class="card card--front-a">
    <div class="brand">
      <span class="brand__dot"></span>
      <span class="brand__name">Quelvane<br>Systems, Inc.</span>
    </div>
    <div class="person">
      <p class="person__name">Marla Dunstead</p>
      <p class="person__title">CEO</p>
    </div>
    <p class="tagline">Design, Develop, Deploy</p>
    <span class="divider"></span>
    <address class="office office--atlanta">
      87 Corliss Avenue, #2291<br>
      Atlanta, GA 30301<br>
      Office: 404.555.0182<br>
      Fax: 404.555.0147<br>
      Mobile: 404.555.0163
    </address>
    <address class="office office--savannah">
      350 West Harrow Bend Road<br>
      Suite 720, Savannah, GA 31401<br>
      Office: 912.555.0139<br>
      Fax: 404.555.0147<br>
      Mobile: 404.555.0163
    </address>
    <p class="email">mdunstead@quelvanesystems.example</p>
    <footer class="web-band">www.quelvanesystems.example</footer>
  </section>

  <section class="card card--back-a">
    <div class="brand brand--large">
      <span class="brand__dot"></span>
      <span class="brand__name">Quelvane<br>Systems, Inc.</span>
    </div>
    <footer class="web-band">www.quelvanesystems.example</footer>
  </section>

  <section class="card card--front-b">
    <div class="person">
      <p class="person__name">Marla Dunstead</p>
      <p class="person__title">CEO</p>
    </div>
    <div class="brand">
      <span class="brand__dot"></span>
      <span class="brand__name">Quelvane<br>Systems, Inc.</span>
    </div>
    <p class="tagline">Design, Develop, Deploy</p>
    <address class="office office--atlanta">
      87 Corliss Avenue, #2291<br>
      Atlanta, GA 30301<br>
      Office: 404.555.0182<br>
      Fax: 404.555.0147<br>
      Mobile: 404.555.0163
    </address>
    <address class="office office--savannah office--right">
      350 West Harrow Bend Road<br>
      Suite 720, Savannah, GA 31401<br>
      Office: 912.555.0139<br>
      Fax: 404.555.0147<br>
      Mobile: 404.555.0163
    </address>
    <footer class="web-band web-band--split">
      <span>www.quelvanesystems.example</span>
      <span>mdunstead@quelvanesystems.example</span>
    </footer>
  </section>

  <section class="card card--back-b">
    <div class="brand brand--large">
      <span class="brand__dot"></span>
      <span class="brand__name">Quelvane<br>Systems, Inc.</span>
    </div>
    <footer class="web-band">www.quelvanesystems.example</footer>
  </section>

</main>
</body>
</html>
```